Live Webcasting Host Wants Template/Theme to Jumpstare Ecommerce Site

Please,Please, Please READ ALL OF THE DESCRIPTION. Thank you.

I need a template for a look for my developer to work with in designing an ecommerce site where clients pay a monthly fee for streaming services and video on demand.

I'll need 2 pages designed:
1) public page
2) client log in landing page.

Please use a CMS (WP preferred) as this will allow is for further content to be added after delivery. Please include the pricing text in boxes in slides (pdf) to help fill out you design for the home page.

The attached slides are to give you a general layout of how I envision the pages. Yes I would like the Client page to be tabbed from the side like in the attached slide.

I've attached company logos for use along with the accompanying .psd and .ai files in the zip. Use the colors in logo in site design.

Thank you for your time.

Please, no designs. This is for a CMS for webpage design like WordPress or Joomla. Thanks. Added Friday, January 13, 2017

Target Market(s)

Churches, Organizations, Civic Organizations, Government Agencies (State, Local) -BUT don't let this deter your creativity. Decision makers/influencers will be video production and/or IT personnel.

Industry/Entity Type

It Company

Font styles to use
Sans Serif

Colors
f5f5f5
e8e8e8
333333
fece3e
cbcbcb
33a6d7
000000

Requirements
Must have
• Responsive Design
Nice to have
• One Page Design
Should not have
• SHOULD NOT HAVE White overall background but use white in other ways if you like.

```html
<!DOCTYPE html>
<html lang="en">
<head>
<meta charset="utf-8">
<title>Lumora — Live Webcasting</title>
<link rel="stylesheet" href="https://fonts.googleapis.com/css2?family=Questrial&family=Montserrat:wght@700;800&display=swap">
<style>
  :root {
    --bg-light: #f5f5f5;
    --ink: #333333;
    --black: #000000;
    --accent: #fece3e;
    --accent-muted: #c9a229;
    --grey-bar: #b9b9b9;
    --white: #ffffff;
  }
  * { margin: 0; padding: 0; box-sizing: border-box; }
  html, body { width: 1200px; height: 1200px; overflow: hidden; }
  body {
    position: relative;
    background: var(--black);
    font-family: "Questrial", sans-serif;
    color: var(--ink);
  }

  /* Header */
  .site-header {
    position: absolute; left: 0; top: 0;
    width: 1200px; height: 177px;
    background: var(--bg-light);
  }
  .brand {
    position: absolute; left: 182px; top: 74px;
    display: flex; align-items: center; gap: 6px;
  }
  .brand-dot {
    width: 10px; height: 10px; border-radius: 50%;
    background: var(--accent);
  }
  .brand-name {
    font-family: "Montserrat", sans-serif;
    font-weight: 800; font-size: 22px; letter-spacing: 0.5px;
    color: var(--black); line-height: 1;
  }
  .nav-link {
    position: absolute; top: 78px;
    font-size: 14.5px; letter-spacing: 0.8px;
    text-transform: uppercase; color: var(--ink);
    transform: translateX(-50%); white-space: nowrap;
  }
  .nav-link.is-active {
    color: var(--accent); font-size: 17.5px; top: 76px;
  }
  .active-bar {
    position: absolute; left: 326px; width: 120px;
    background: var(--accent);
  }
  .active-bar.top { top: 0; height: 6px; }
  .active-bar.bottom { top: 170px; height: 7px; }
  .login-button {
    position: absolute; left: 885px; top: 15px;
    width: 142px; height: 32px; border-radius: 16px;
    background: var(--ink); color: var(--white);
    font-size: 16px; letter-spacing: 1.5px;
    display: flex; align-items: center; justify-content: center;
  }

  /* Hero slider */
  .hero {
    position: absolute; left: 0; top: 177px;
    width: 1200px; height: 635px;
    background: radial-gradient(ellipse 40% 55% at 68% 55%, #8a8a8a 0%, #4a4a4a 40%, #121212 75%, #050505 100%);
  }
  .slider-arrow {
    position: absolute; top: 289px; width: 74px; height: 132px;
  }
  .slider-arrow.prev { left: 70px; }
  .slider-arrow.next { left: 1054px; }
  .slider-dots {
    position: absolute; left: 543px; top: 592px;
    display: flex; gap: 23px;
  }
  .slider-dot {
    width: 22px; height: 22px; border-radius: 50%;
    background: var(--accent);
  }
  .slider-dot.is-current {
    background: var(--bg-light);
    border: 3px solid var(--accent);
  }

  /* Pricing */
  .pricing {
    position: absolute; left: 0; top: 812px;
    width: 1200px; height: 317px;
    background: var(--black);
  }
  .plan-card {
    position: absolute; top: 33px;
    width: 270px; height: 255px;
    border: 3px solid var(--white);
    overflow: hidden;
    text-align: center;
  }
  .plan-card.small { left: 181px; }
  .plan-card.medium { left: 466px; }
  .plan-card.large { left: 750px; }
  .plan-visual {
    position: absolute; inset: 0;
    background: radial-gradient(circle at 55% 52%, #7fae3a 0%, #2f6e2a 18%, #16341a 34%, #0c0f0c 52%, #2a2a2a 64%, #0b0b0b 80%);
  }
  .plan-name {
    position: absolute; left: 7px; top: 7px;
    font-family: "Montserrat", sans-serif; font-weight: 700;
    font-size: 16px; color: var(--white);
  }
  .plan-price {
    position: absolute; left: 0; right: 0; top: 22px;
    font-family: "Montserrat", sans-serif; font-weight: 800;
    font-size: 30px; color: var(--accent);
  }
  .plan-card.small .plan-price { right: 8px; top: 16px; }
  .plan-hours {
    position: absolute; left: 0; right: 0; top: 102px;
    font-size: 23px; color: var(--white); letter-spacing: 0.6px;
    white-space: nowrap;
  }
  .plan-card.small .plan-hours { top: 99px; }
  .plan-usage {
    position: absolute; left: 0; right: 0; top: 131px;
    font-size: 19.5px; line-height: 15px; color: var(--accent);
    letter-spacing: 0.5px; white-space: nowrap;
  }
  .plan-card.small .plan-usage { top: 134px; }
  .plan-storage {
    position: absolute; left: 0; right: 0; bottom: 0;
    height: 35px; background: var(--grey-bar);
    display: flex; align-items: center; justify-content: center;
    font-size: 16.5px; color: var(--ink); white-space: nowrap;
  }

  /* Footer */
  .site-footer {
    position: absolute; left: 0; top: 1129px;
    width: 1200px; height: 71px;
    background: var(--bg-light);
    display: flex; align-items: center; justify-content: center;
  }
  .copyright {
    font-size: 16px; letter-spacing: 1.6px; color: var(--black);
    text-transform: uppercase; margin-left: -36px;
  }
</style>
</head>
<body>
  <header class="site-header">
    <span class="active-bar top"></span>
    <div class="brand">
      <span class="brand-name">LUMORA</span>
      <span class="brand-dot"></span>
    </div>
    <nav>
      <a class="nav-link is-active" style="left:386px">Features</a>
      <a class="nav-link" style="left:529px">Pricing</a>
      <a class="nav-link" style="left:671px">About Us</a>
      <a class="nav-link" style="left:814px">Webcasting 101</a>
      <a class="nav-link" style="left:956px">Contact</a>
    </nav>
    <a class="login-button">LOG IN</a>
    <span class="active-bar bottom"></span>
  </header>

  <section class="hero" role="img" aria-label="Black and white photograph of a tiger's face on a dark background">
    <svg class="slider-arrow prev" viewBox="0 0 74 132" aria-hidden="true">
      <polyline points="64,10 12,66 64,122" fill="none" stroke="var(--accent-muted)" stroke-width="20" stroke-linecap="round" stroke-linejoin="round"/>
    </svg>
    <svg class="slider-arrow next" viewBox="0 0 74 132" aria-hidden="true">
      <polyline points="10,10 62,66 10,122" fill="none" stroke="var(--accent-muted)" stroke-width="20" stroke-linecap="round" stroke-linejoin="round"/>
    </svg>
    <div class="slider-dots">
      <span class="slider-dot"></span>
      <span class="slider-dot is-current"></span>
      <span class="slider-dot"></span>
    </div>
  </section>

  <section class="pricing">
    <article class="plan-card small">
      <div class="plan-visual" role="img" aria-label="Close-up of a camera lens"></div>
      <h3 class="plan-name">Small</h3>
      <p class="plan-price">$49</p>
      <p class="plan-hours">400 viewer hours</p>
      <p class="plan-usage">(50 Viewers watching<br>2 hrs-4 times per month)</p>
      <p class="plan-storage">100 GB/month of video Storage</p>
    </article>
    <article class="plan-card medium">
      <div class="plan-visual" role="img" aria-label="Close-up of a camera lens"></div>
      <h3 class="plan-name">Medium</h3>
      <p class="plan-price">$399</p>
      <p class="plan-hours">4000 viewer hours</p>
      <p class="plan-usage">(500 Viewers watching<br>2 hrs-4 times per month)</p>
      <p class="plan-storage">500 GB/month of video</p>
    </article>
    <article class="plan-card large">
      <div class="plan-visual" role="img" aria-label="Close-up of a camera lens"></div>
      <h3 class="plan-name">Large</h3>
      <p class="plan-price">$999</p>
      <p class="plan-hours">4000 viewer hours</p>
      <p class="plan-usage">(2000 Viewers watching<br>2 hrs- 4 times per month)</p>
      <p class="plan-storage">2000 GB/month of video</p>
    </article>
  </section>

  <footer class="site-footer">
    <p class="copyright">Copyright© 2017Northlane All Right Reserved.</p>
  </footer>
</body>
</html>
```